The Maple Sprout Clinic needs a Letterhead

We are a bilingual pediatric clinic located in Montreal, Canada.

Our english name is Maple Sprout Clinic
Our french name is Clinique du petit ruisseau

We offer complete care for children including general pediatric care, pediatric specialist care such as Ear, Nose and Throat, Urology, Neurology and Adolescent Medicine. We also have paramedical specialists such as psychologists, social workers, occupational therapists, speech and language pathologists.

The letterhead must use and be harmonious with our new logo. See Design #4923293. We need two types of letterhead. One for a the Logo and both english and french names on the top and the second with the list of current staff on the left. I have uploaded two old examples for you to see. Thanks and good luck.

Font styles to use
Sans Serif

Colors
3176b5
9d9d9d

Requirements
Must have
• Include our logo.
Nice to have
• Most of our printing is done in black and white. So a grayscale design is fine.
I have included a color and grayscale versions of our logo.

We prefer clean modern designs.

```html
<!DOCTYPE html>
<html lang="fr">
<head>
<meta charset="utf-8">
<title>Maple Sprout Clinic — Letterhead</title>
<link rel="stylesheet" href="https://fonts.googleapis.com/css2?family=Arimo&family=Source+Sans+3:wght@400;700&display=swap">
<style>
  :root {
    --paper: #ffffff;
    --frame: #d6d6d6;
    --brand-grey: #8f8f8f;
    --label-grey: #9d9d9d;
    --ink: #111111;
    --bar: #000000;
  }
  * { margin: 0; padding: 0; box-sizing: border-box; }
  html, body {
    width: 900px; height: 1200px; overflow: hidden;
    background: var(--paper);
  }
  .letterhead {
    position: relative;
    width: 900px; height: 1200px;
  }
  .page-frame {
    position: absolute;
    left: 41px; top: 22px;
    width: 819px; height: 1159px;
    border: 1px solid var(--frame);
  }
  .brand {
    position: absolute;
    top: 70px; left: 0; width: 900px;
    display: flex; justify-content: center; align-items: center; gap: 14px;
    font-family: "Arimo", Arial, sans-serif;
    font-size: 19px; line-height: 21px;
    color: var(--brand-grey);
    letter-spacing: -0.3px;
  }
  .brand-name-fr { text-align: right; width: 150px; }
  .brand-name-en { text-align: left; width: 150px; }
  .brand-dot {
    width: 64px; height: 64px; border-radius: 50%;
    background: var(--brand-grey);
  }
  .side-bar {
    position: absolute;
    left: 41px; top: 1068px;
    width: 22px; height: 113px;
    background: var(--bar);
  }
  .address {
    position: absolute;
    left: 81px; top: 1066px;
    font-family: "Source Sans 3", "Myriad Pro", sans-serif;
    font-size: 9px; line-height: 11.2px;
    color: var(--ink);
  }
  .address-label { font-weight: 700; }
  .address-label-en { font-weight: 700; color: var(--label-grey); margin-bottom: 6px; }
  .address strong { font-weight: 700; }
</style>
</head>
<body>
<main class="letterhead">
  <div class="page-frame"></div>

  <header class="brand">
    <div class="brand-name-fr">Clinique<br>du petit<br>ruisseau</div>
    <div class="brand-dot"></div>
    <div class="brand-name-en">Maple<br>Sprout<br>Clinic</div>
  </header>

  <div class="side-bar"></div>

  <footer class="address">
    <p class="address-label">ADDRESSE</p>
    <p class="address-label-en">ADDRESS</p>
    <p>2215 boul. des Érables</p>
    <p>Suite 200</p>
    <p>Pointe-Claire, Qc</p>
    <p>H9R 2K8</p>
    <p><strong>Tél.</strong> (514) 555-0142</p>
    <p><strong>Fax.</strong> (514) 555-0187</p>
  </footer>
</main>
</body>
</html>
```